8" x 11" One Page Flyer for Fence Installation Company

We are looking to promote our business with a new flyer that would be handed out in person to people or put at their mailbox/door at their homes. The flyer needs to be creative and attention-grabbing. I have attached some of our previous flyers and our website information. Do not call or email regarding the flyer. We want the flyer to look professional but also friendly. One page, NOT folded. You can use images from our website at www.MyBraxtonYard.com or our Facebook page at www.Facebook.com/HollowbrookRailsBKT. We are flexible with what photos you can use but there must be photos of OUR fences on the flyer. More photos specifically can also be provided. Colors need to be suitable for a flyer printed on canary yellow in color paper OR white paper.

Target Market(s)

Homeowners that need a new fence

Industry/Entity Type

Construction

Font styles to use
Sans Serif
Other font styles liked:
• HD Colton

Colors
0054AA
0677BA
7BADD7
CADEEF
E8F1F8
0094D4
00A9DD
6FCCEA
C7EBF8
E9F6FB

Requirements
Must have
• Our fence photos - mostly wood fence photos (different designs), SIZE SHOULD BE LETTER SIZE 8" x 11"
Nice to have
• A nice bible verse featured at the bottom of the flyer.
Should not have
• DO NOT COPY THE WEBSITE FORMAT, I WANT SOMETHING UNIQUE. Other people's fence photos, they must all come from our website or facebook page

```html
<!DOCTYPE html>
<html lang="en">
<head>
<meta charset="utf-8">
<title>Hollowbrook Rails – Fence Flyer</title>
<link href="https://fonts.googleapis.com/css2?family=Poppins:wght@400;500;600;700;800&family=Montserrat:wght@500;600;700&display=swap" rel="stylesheet">
<style>
  :root{
    --stage:#2f2a8e;
    --paper:#ffffff;
    --brown:#5b3f22;
    --brown-dark:#4a3119;
    --orange:#e8912f;
    --blue:#3f6fba;
    --sky:#3a86c8;
    --ink:#1c1c1c;
    --cream:#ffffff;
  }
  *{margin:0;padding:0;box-sizing:border-box}
  html,body{width:1200px;height:870px;overflow:hidden;background:var(--stage)}
  body{font-family:"Poppins",sans-serif}
  .flyer{position:absolute;left:295px;top:20px;width:609px;height:830px;background:var(--paper);overflow:hidden}
  .flyer-bg{position:absolute;inset:0}
  .headline{position:absolute;left:39px;top:26px;line-height:1}
  .headline .we-build{font-weight:700;font-size:29px;color:var(--sky);letter-spacing:.5px}
  .headline .fences{font-weight:800;font-size:45px;color:var(--brown-dark);letter-spacing:8px;margin-top:2px;display:flex;align-items:flex-end}
  .headline .fences .dots{display:flex;gap:3px;margin-left:-2px;margin-bottom:5px}
  .headline .fences .dots i{display:block;width:7px;height:7px;background:var(--orange)}
  .headline .tagline{font-family:"Montserrat",sans-serif;font-weight:500;font-size:15.5px;color:var(--ink);margin-top:6px;letter-spacing:.1px}
  .brand{position:absolute;left:418px;top:38px;text-align:left}
  .brand-name{font-weight:700;font-size:15.5px;color:var(--brown-dark);line-height:1.2}
  .brand-phone{font-family:"Montserrat",sans-serif;font-weight:600;font-size:13px;color:var(--ink);line-height:1.3}
  .col-why{position:absolute;left:60px;top:200px;width:300px;color:var(--cream)}
  .section-title{font-weight:700;font-size:21px;color:var(--orange);line-height:1.2}
  .why-lead{font-family:"Montserrat",sans-serif;font-weight:700;font-size:14.5px;line-height:1.2;margin-top:3px}
  .benefits{list-style:none;margin-top:10px;font-family:"Montserrat",sans-serif;font-weight:500;font-size:12.6px}
  .benefits li{height:16.5px;position:relative;padding-left:14px}
  .benefits li::before{content:"";position:absolute;left:0;top:6px;width:5px;height:5px;border-radius:50%;background:var(--orange)}
  .rule-h{position:absolute;left:60px;top:412px;width:308px;border-top:1px dashed var(--orange)}
  .rule-v{position:absolute;left:368px;top:162px;height:334px;border-left:1px dashed var(--orange)}
  .showroom{position:absolute;left:60px;top:418px;width:310px;color:var(--cream);font-family:"Montserrat",sans-serif}
  .showroom h3{font-weight:700;font-size:14.5px;line-height:1.3}
  .showroom p{font-weight:600;font-size:12px;line-height:18.5px;margin-top:4px}
  .showroom .hi{color:var(--orange)}
  .col-where{position:absolute;left:388px;top:200px;width:200px;text-align:center;color:var(--cream)}
  .address{font-family:"Montserrat",sans-serif;font-weight:700;font-size:13.5px;line-height:17.5px;margin-top:3px}
  .map{position:absolute;left:406px;top:276px;width:164px;height:196px;border:4px solid var(--orange);border-radius:12px;background:linear-gradient(160deg,#eef0f2,#dfe4e8)}
  .gallery{position:absolute;left:42px;top:503px;width:528px;height:264px;background:var(--paper)}
  .photo{position:absolute}
  .p1{left:8px;top:8px;width:148px;height:120px;background:linear-gradient(180deg,#b9a98a,#d8cba6 60%,#8a8e5a)}
  .p2{left:8px;top:136px;width:148px;height:120px;background:linear-gradient(180deg,#c7cbd3,#d3b278 40%,#b98e4e)}
  .p3{left:163px;top:8px;width:202px;height:248px;background:linear-gradient(180deg,#dcdde0,#cdbd95 35%,#8a7150 75%,#5f4a34)}
  .p4{left:371px;top:8px;width:149px;height:120px;background:linear-gradient(180deg,#a9c3de,#d5c9a6 40%,#a69776)}
  .p5{left:371px;top:136px;width:149px;height:120px;background:linear-gradient(180deg,#b9c8d8,#3b3631 40%,#8c6c4c)}
  .contact{position:absolute;left:42px;top:786px;width:528px;display:flex;justify-content:space-between;align-items:center;color:var(--cream);font-family:"Montserrat",sans-serif;font-weight:700;font-size:11.4px;white-space:nowrap}
  .contact span{display:flex;align-items:center;gap:4px}
  .contact svg{width:11px;height:11px}
</style>
</head>
<body>
<main class="flyer">
  <svg class="flyer-bg" viewBox="0 0 609 830" aria-hidden="true">
    <polygon points="0,150 284,157 609,118 609,830 0,830" fill="var(--brown)"/>
    <polygon points="0,150 284,157 0,196" fill="var(--orange)"/>
    <polygon points="0,551 609,613 609,683 0,747" fill="var(--orange)"/>
    <polygon points="0,747 609,680 609,830 0,830" fill="var(--blue)"/>
  </svg>

  <header class="headline">
    <div class="we-build">WE BUILD</div>
    <div class="fences">FENCES<span class="dots"><i></i><i></i><i></i><i></i></span></div>
    <p class="tagline">And we would love to build your fence too!</p>
  </header>

  <div class="brand">
    <div class="brand-name">Hollowbrook Rails</div>
    <div class="brand-phone">555-014-2290</div>
  </div>

  <section class="col-why">
    <h2 class="section-title">WHY CHOOSE US?</h2>
    <p class="why-lead">Beautiful, professionally installed<br>fences at affordable prices!</p>
    <ul class="benefits">
      <li>Free Estimates</li>
      <li>Professional Installation</li>
      <li>Concrete in EVERY Post</li>
      <li>HOA Submission Assistance</li>
      <li>Lifetime Workmanship Warranty</li>
      <li>Experienced Installation Teams</li>
      <li>Quality Workmanship &amp; Materials</li>
      <li>FREE Gate Adjustments for LIFE</li>
    </ul>
  </section>
  <div class="rule-h"></div>
  <div class="rule-v"></div>

  <section class="showroom">
    <h3>Visit our indoor &amp; outdoor showroom!</h3>
    <p>Our outdoor showroom is open <span class="hi">24/7</span>,<br>
    while our indoor showroom and office is open<br>
    <span class="hi">Monday -Thurs 9 AM - 3 &nbsp;PM, Friday 9 AM-1 PM</span></p>
  </section>

  <section class="col-where">
    <h2 class="section-title">WHERE ARE WE?</h2>
    <p class="address">417 Quarry Ln<br>Braxton, NC 28999</p>
  </section>
  <div class="map" role="img" aria-label="Street map showing the showroom location"></div>

  <section class="gallery">
    <div class="photo p1" role="img" aria-label="Photo of a shadowbox wood privacy fence"></div>
    <div class="photo p2" role="img" aria-label="Photo of a wooden picket fence with company sign"></div>
    <div class="photo p3" role="img" aria-label="Photo of a long scalloped wood privacy fence along a backyard"></div>
    <div class="photo p4" role="img" aria-label="Photo of a wooden privacy fence with double gate"></div>
    <div class="photo p5" role="img" aria-label="Photo of a black aluminum rail fence"></div>
  </section>

  <footer class="contact">
    <span><svg viewBox="0 0 24 24" fill="none" stroke="currentColor" stroke-width="2.4"><path d="M5 3h4l2 5-3 2a12 12 0 0 0 6 6l2-3 5 2v4a2 2 0 0 1-2 2A18 18 0 0 1 3 5a2 2 0 0 1 2-2z"/></svg>555-014-2290</span>
    <span>|</span>
    <span><svg viewBox="0 0 24 24" fill="currentColor"><path d="M2 5h20v14H2z"/><path d="M2 5l10 8 10-8" stroke="var(--blue)" stroke-width="2" fill="none"/></svg>office@mybraxtonyard.com</span>
    <span>|</span>
    <span><svg viewBox="0 0 24 24" fill="none" stroke="currentColor" stroke-width="2"><circle cx="12" cy="12" r="10"/><path d="M2 12h20M12 2c3 3 3 17 0 20M12 2c-3 3-3 17 0 20"/></svg>www.MyBraxtonYard.com</span>
  </footer>
</main>
</body>
</html>
```